BHSC Business cards

We are an established dental practice that is looking for new business cards to match our new logo. We are looking for something unique and sophisticated.
BRIEF: Colours are black, silver and white. Include the company name, logo (including “Pelwick Heath Dental Care”) and phone number “03 9415 2876”.
Front - Include the company name, logo (including “Pelwick Heath Dental Care”) and phone number “03 9415 2876”.
Back - Include the company name,  “Pelwick Heath Dental Care”, phone number “03 9415 2876”. address "64A Tindle Street, Pelwick Heath, Vic 3187", "Email reception@pelwickheathdentalcare.com.au", the Dentist Name " Dr ................................"  Your next appointment "Day, date and time(am/pm)".  3 lines for 3 appointments please, and at the bottom "IF UNABLE TO KEEP THIS APPOINTMENT 48 HOURS NOTICE IS REQUIRED."
Try and be creative and different with the design, i've added an image for inspiration

Target Market(s)
ALL in need of dental
Industry/Entity Type
Dental Clinic
Look and feel
Each slider illustrates characteristics of the customer's brand and the style your logo design should communicate.

```html
<!DOCTYPE html>
<html lang="en">
<head>
<meta charset="utf-8">
<title>Pelwick Heath Dental Care — Business Cards</title>
<link rel="stylesheet" href="https://fonts.googleapis.com/css2?family=Barlow:wght@500;600&family=Quicksand:wght@500&display=swap">
<style>
  :root {
    --page-bg: #dcdcdc;
    --card-bg: #f7f7f7;
    --wash-light: #f8f8f8;
    --wash-mid: #ededed;
    --ink: #9b9b9b;
    --ink-dark: #8a8a8a;
    --rule: #a6a6a6;
  }
  * { box-sizing: border-box; margin: 0; padding: 0; }
  html, body { width: 1200px; height: 900px; overflow: hidden; }
  body {
    background: var(--page-bg);
    display: flex; flex-direction: column; align-items: center; justify-content: center;
    gap: 56px;
    font-family: "Quicksand", sans-serif;
    color: var(--ink);
  }
  .card {
    position: relative;
    width: 622px; height: 380px;
    background: var(--card-bg);
    overflow: hidden;
    box-shadow: 0 6px 18px rgba(0,0,0,.18);
  }
  .card-texture {
    position: absolute; inset: 0;
    background: linear-gradient(135deg, var(--wash-light) 0%, var(--wash-mid) 50%, var(--wash-light) 100%);
  }
  .card-content { position: relative; height: 100%; }

  .brand { display: flex; align-items: center; font-family: "Barlow", sans-serif; font-weight: 600; color: var(--ink); }
  .brand-mark { border: 4px solid var(--ink); border-radius: 50%; flex: none; }
  .brand-name { text-transform: uppercase; line-height: 1; }
  .brand-name .line-sub { display: block; letter-spacing: .28em; }

  /* Front */
  .card-front .card-content { display: flex; align-items: center; justify-content: center; }
  .card-front .brand { gap: 18px; }
  .card-front .brand-mark { width: 64px; height: 64px; }
  .card-front .brand-name { font-size: 36px; letter-spacing: .05em; }
  .card-front .brand-name .line-sub { font-size: 15px; margin-top: 6px; }

  /* Back */
  .card-back .card-content { padding: 22px 26px 0; }
  .back-header { display: flex; justify-content: space-between; align-items: flex-start; height: 58px; }
  .card-back .brand { gap: 10px; }
  .card-back .brand-mark { width: 30px; height: 30px; border-width: 3px; }
  .card-back .brand-name { font-size: 17px; letter-spacing: .03em; }
  .card-back .brand-name .line-sub { font-size: 8px; margin-top: 3px; letter-spacing: .22em; }
  .contact-list { list-style: none; font-size: 11.5px; line-height: 1.75; color: var(--ink-dark); }
  .contact-list li { display: flex; align-items: center; gap: 7px; }
  .contact-list svg { width: 13px; height: 13px; flex: none; }
  .header-rule { border: 0; border-top: 2px solid var(--rule); margin: 0 -26px; }

  .appointment-form { padding: 22px 34px 0 38px; font-size: 19px; color: var(--ink-dark); }
  .form-row { display: flex; align-items: baseline; height: 38px; }
  .form-row .dots { flex: 1; border-bottom: 2px dotted var(--ink); margin: 0 4px; transform: translateY(-3px); }
  .form-row .dots.short { flex: .8; }
  .row-dentist { padding-left: 60px; padding-right: 50px; }

  .notice {
    text-align: center; font-family: "Barlow", sans-serif; font-weight: 500;
    font-size: 18px; letter-spacing: .06em; line-height: 1.25; color: var(--ink);
    margin-top: 16px; text-transform: uppercase;
  }
</style>
</head>
<body>

<section class="card card-front" aria-label="Business card front">
  <div class="card-texture" role="img" aria-label="Faint crossing line pattern in light silver"></div>
  <div class="card-content">
    <div class="brand">
      <span class="brand-mark" aria-hidden="true"></span>
      <div class="brand-name">
        <span class="line-main">Pelwick Heath</span>
        <span class="line-sub">Dental Care — 03 9415 2876</span>
      </div>
    </div>
  </div>
</section>

<section class="card card-back" aria-label="Business card back">
  <div class="card-texture" role="img" aria-label="Faint crossing line pattern in light silver"></div>
  <div class="card-content">
    <header class="back-header">
      <div class="brand">
        <span class="brand-mark" aria-hidden="true"></span>
        <div class="brand-name">
          <span class="line-main">Pelwick Heath</span>
          <span class="line-sub">Dental Care — 03 9415 2876</span>
        </div>
      </div>
      <ul class="contact-list">
        <li>
          <svg viewBox="0 0 24 24" fill="none" stroke="#8a8a8a" stroke-width="2"><path d="M12 22s7-7.5 7-13a7 7 0 0 0-14 0c0 5.5 7 13 7 13z"/><circle cx="12" cy="9" r="2.5"/></svg>
          64A Tindle Street, Pelwick Heath, Vic 3187
        </li>
        <li>
          <svg viewBox="0 0 24 24" fill="none" stroke="#8a8a8a" stroke-width="2"><rect x="2" y="5" width="20" height="14"/><path d="M2 5l10 8 10-8"/></svg>
          reception@pelwickheathdentalcare.com.au
        </li>
      </ul>
    </header>
    <hr class="header-rule">

    <div class="appointment-form">
      <div class="form-row row-dentist"><span>Dentist Name: Dr.</span><span class="dots"></span></div>
      <div class="form-row"><span>Date</span><span class="dots short"></span><span>At</span><span class="dots"></span><span>am/pm</span></div>
      <div class="form-row"><span>Date</span><span class="dots short"></span><span>At</span><span class="dots"></span><span>am/pm</span></div>
      <div class="form-row"><span>Date</span><span class="dots short"></span><span>At</span><span class="dots"></span><span>am/pm</span></div>
    </div>

    <p class="notice">If unable to keep this appointment<br>48 hours notice is required.</p>
  </div>
</section>

</body>
</html>
```